Tidewell Outdoor Signage

We need an outdoor signage design for my company with new logo designed from makerhive. We do electrical, Air conditioning & Plumbing, installation, service, repairs and maintenance. The design shall be an eye catching that cannot miss ready it.

Industry/Entity Type

Electrical, Air conditioning, Plumbing

```html
<!DOCTYPE html>
<html lang="en">
<head>
<meta charset="utf-8">
<title>Tidewell Outdoor Signage</title>
<link rel="stylesheet" href="https://fonts.googleapis.com/css2?family=Poppins:ital,wght@0,500;0,600;0,700;1,400;1,800&display=swap">
<style>
  :root {
    --backdrop: #606060;
    --white: #ffffff;
    --blue: #1b6ab0;
    --orange: #f38d3f;
    --red: #ec1f2c;
    --ink: #3a3a3a;
    --ghost: #f1f1f1;
  }
  html, body { margin: 0; padding: 0; overflow: hidden; }
  body {
    width: 1200px; height: 1200px;
    background: var(--backdrop);
    position: relative;
    font-family: "Poppins", sans-serif;
  }
  .sign {
    position: absolute; left: 200px; top: 400px;
    width: 800px; height: 400px;
    background: var(--white);
    overflow: hidden;
  }
  .sign-bands { position: absolute; inset: 0; }
  .tagline {
    position: absolute; left: 33px; top: 44px; margin: 0;
    font-size: 22px; line-height: 28px; font-style: italic; font-weight: 400;
    color: var(--ink); letter-spacing: 0.3px;
  }
  .tagline strong { font-weight: 800; }
  .hero-art {
    position: absolute; left: 48px; top: 153px; width: 314px; height: 236px;
    border-radius: 50% 40% 45% 50%;
    background: linear-gradient(135deg, var(--orange) 0%, var(--red) 50%, var(--blue) 100%);
    opacity: 0.9;
  }
  .brand {
    position: absolute; left: 575px; top: 28px; width: 215px;
    text-align: center;
  }
  .brand-dot {
    width: 64px; height: 64px; border-radius: 50%;
    background: var(--orange); margin: 0 auto 6px;
  }
  .brand-name {
    font-size: 44px; font-weight: 600; color: var(--orange);
    line-height: 1; margin: 0;
  }
  .brand-services {
    font-size: 9.5px; font-weight: 600; color: var(--blue);
    margin: 4px 0 0; letter-spacing: 0.2px;
  }
  .contact {
    position: absolute; right: 0; height: 44px;
    background: var(--red); color: var(--white);
    border-radius: 22px 0 0 22px;
    display: flex; align-items: center;
    font-size: 20px; font-weight: 500;
  }
  .contact-email { top: 190px; width: 403px; }
  .contact-phone { top: 253px; width: 216px; font-weight: 600; }
  .contact-icon {
    width: 30px; height: 30px; border-radius: 50%; background: var(--white);
    margin: 0 22px 0 9px; display: flex; align-items: center; justify-content: center;
    flex-shrink: 0;
  }
  .website {
    position: absolute; right: 29px; top: 358px;
    color: var(--white); font-size: 20px; font-weight: 600;
  }
</style>
</head>
<body>
  <div class="sign">
    <svg class="sign-bands" viewBox="0 0 800 400" width="800" height="400" aria-hidden="true">
      <polygon points="0,0 476,0 452,15 0,15" fill="var(--orange)"/>
      <polygon points="0,0 476,0 459,10 0,10" fill="var(--blue)"/>
      <path d="M0,160 C-10,240 30,330 90,400 L0,400 Z" fill="var(--ghost)"/>
      <path d="M320,280 C420,230 520,250 600,300 C520,290 420,290 320,280 Z" fill="var(--ghost)"/>
      <path d="M0,290 C5,350 30,385 60,400 L0,400 Z" fill="var(--blue)"/>
      <path d="M25,320 C35,360 50,385 70,400 L92,400 C60,380 38,350 25,320 Z" fill="var(--orange)"/>
      <path d="M310,400 C380,390 420,360 500,340 C560,330 640,328 800,326 L800,400 Z" fill="var(--blue)"/>
      <path d="M372,366 C450,330 560,320 800,314 L800,326 C640,328 560,330 500,340 C450,348 410,356 372,366 Z" fill="var(--orange)"/>
      <path d="M580,320 C650,314 720,310 800,310 L800,314 C720,316 650,318 580,320 Z" fill="var(--orange)"/>
      <path d="M585,322 C660,316 730,312 800,310 L800,303 C720,306 650,312 585,322 Z" fill="var(--orange)"/>
    </svg>

    <p class="tagline">“<strong>QUICK &amp; EXCELLENT</strong> SERVICE FOR YOUR<br><strong>ELECTRICAL</strong>, <strong>AIR CONDITIONING</strong>,<br>&amp; <strong>PLUMBING</strong> NEEDS”</p>

    <div class="hero-art" role="img" aria-label="Large emblem artwork: tap, lightning bolt and pipes in orange, red and blue"></div>

    <div class="brand">
      <div class="brand-dot"></div>
      <p class="brand-name">Tidewell</p>
      <p class="brand-services">Electrical &nbsp;Air Conditioning &nbsp;Plumbing</p>
    </div>

    <div class="contact contact-email">
      <span class="contact-icon">
        <svg width="18" height="13" viewBox="0 0 18 13" aria-hidden="true"><rect x="1" y="1" width="16" height="11" rx="1" fill="none" stroke="var(--red)" stroke-width="1.6"/><path d="M1,1 L9,7.5 L17,1 M1,12 L7,6 M17,12 L11,6" fill="none" stroke="var(--red)" stroke-width="1.4"/></svg>
      </span>
      info@tidewellelectrical.com.au
    </div>

    <div class="contact contact-phone">
      <span class="contact-icon">
        <svg width="16" height="16" viewBox="0 0 24 24" aria-hidden="true"><path d="M6.6 10.8a15.1 15.1 0 0 0 6.6 6.6l2.2-2.2a1 1 0 0 1 1-.25 11.4 11.4 0 0 0 3.6.57 1 1 0 0 1 1 1V20a1 1 0 0 1-1 1A17 17 0 0 1 3 4a1 1 0 0 1 1-1h3.5a1 1 0 0 1 1 1c0 1.25.2 2.45.57 3.57a1 1 0 0 1-.25 1z" fill="var(--red)"/></svg>
      </span>
      0400 555 182
    </div>

    <div class="website">www.tidewellelectrical.com.au</div>
  </div>
</body>
</html>
```